Business card for medical clinic

I need an upmarket, modern medical/health business card for my clinic

Contact Information for Business Card

name, address, email, qr code

```html
<!DOCTYPE html>
<html lang="en">
<head>
<meta charset="utf-8">
<title>Meridian Care Partners – Business Card</title>
<link rel="stylesheet" href="https://fonts.googleapis.com/css2?family=Cinzel:wght@500&family=Noto+Serif:wght@400&display=swap">
<style>
  :root {
    --backdrop: #6a6a6c;
    --card-dark: #161616;
    --card-light: #ffffff;
    --brand-blue: #1b8fd2;
    --name-blue: #1a5d8c;
    --ink: #2b2b2b;
    --icon-blue: #1f6fa8;
  }
  * { box-sizing: border-box; margin: 0; padding: 0; }
  html, body {
    width: 900px;
    height: 1200px;
    overflow: hidden;
    background: var(--backdrop);
  }
  .canvas {
    position: relative;
    width: 900px;
    height: 1200px;
  }
  .card {
    position: absolute;
    left: 133px;
    width: 633px;
    height: 364px;
  }
  .card-front {
    top: 210px;
    background: var(--card-dark);
    display: flex;
    align-items: center;
    justify-content: center;
  }
  .brand {
    display: flex;
    align-items: center;
    gap: 14px;
  }
  .brand-dot {
    width: 16px;
    height: 16px;
    border-radius: 50%;
    background: var(--brand-blue);
  }
  .brand-name {
    font-family: "Cinzel", serif;
    font-weight: 500;
    font-size: 27px;
    letter-spacing: 1px;
    color: var(--brand-blue);
  }
  .card-back {
    top: 624px;
    background: var(--card-light);
  }
  .contact-block {
    position: absolute;
    left: 202px;
    top: 78px;
    font-family: "Noto Serif", serif;
    color: var(--ink);
  }
  .person-name {
    font-family: "Cinzel", serif;
    font-weight: 500;
    font-size: 21px;
    color: var(--name-blue);
    letter-spacing: 0.5px;
    line-height: 1.1;
  }
  .person-title {
    font-size: 15px;
    margin-top: 3px;
  }
  .address {
    margin-top: 16px;
    font-size: 15px;
    line-height: 22px;
    font-style: normal;
  }
  .contact-list {
    list-style: none;
    margin-top: 14px;
    font-size: 15px;
  }
  .contact-list li {
    display: flex;
    align-items: center;
    gap: 6px;
    height: 24px;
  }
  .contact-list .phone { letter-spacing: 3px; }
  .contact-icon { width: 12px; height: 12px; flex: none; }
</style>
</head>
<body>
<main class="canvas">
  <section class="card card-front">
    <div class="brand">
      <span class="brand-dot"></span>
      <span class="brand-name">MERIDIAN CARE PARTNERS</span>
    </div>
  </section>

  <section class="card card-back">
    <div class="contact-block">
      <h1 class="person-name">DANIEL WHITFORD</h1>
      <p class="person-title">Principal Consultant</p>
      <address class="address">
        PO Box 418205<br>
        Juniper Falls, Oregon 97321
      </address>
      <ul class="contact-list">
        <li class="phone">
          <svg class="contact-icon" viewBox="0 0 12 12" aria-hidden="true">
            <path d="M2.2 0.8 L4 0.8 L4.8 3.2 L3.6 4.2 Q4.8 6.9 7.6 8.4 L8.7 7.2 L11.2 8 L11.2 9.8 Q11 11.2 9.6 11.2 Q1 10.5 0.8 2.2 Q0.8 0.8 2.2 0.8 Z" fill="var(--icon-blue)"/>
          </svg>
          +1-555-204-6391
        </li>
        <li>
          <svg class="contact-icon" viewBox="0 0 12 12" aria-hidden="true">
            <rect x="0.5" y="2" width="11" height="8" fill="var(--icon-blue)"/>
            <path d="M0.8 2.4 L6 6.6 L11.2 2.4" fill="none" stroke="#fff" stroke-width="1"/>
          </svg>
          info@meridiancarepartners.com
        </li>
        <li>
          <svg class="contact-icon" viewBox="0 0 12 12" aria-hidden="true">
            <g fill="none" stroke="var(--icon-blue)" stroke-width="1">
              <circle cx="6" cy="6" r="5.2"/>
              <ellipse cx="6" cy="6" rx="2.3" ry="5.2"/>
              <line x1="0.8" y1="6" x2="11.2" y2="6"/>
              <line x1="6" y1="0.8" x2="6" y2="11.2"/>
            </g>
          </svg>
          www.meridiancarepartners.com
        </li>
      </ul>
    </div>
  </section>
</main>
</body>
</html>
```